New Zealand Luggage Importer Needs Business Cards

We need professional, creative and fashionable business cards created.
We are based in New Zealand and import and distribute high-end, quality, fashionable and durable luggage.
We pride ourselves on selling the very best quality luggage, second only to 1 brand (which we won't mention here)...we use the same manufacturer. However, our prices are much more reasonable.
Industry/Entity Type
Business
Contact Information for Business Card
Mark Dunsley
027 512 4068
3/17 Harlow Street, Pinecrest Flats, Auckland, 0614
PO Box 204377, Fernside, Auckland 0731
09-528-3916
sales@brivancases.co.nz / www.brivancases.co.nz

```html
<!DOCTYPE html>
<html lang="en">
<head>
<meta charset="utf-8">
<title>Brivan Cases — Business Cards</title>
<link href="https://fonts.googleapis.com/css2?family=Michroma&family=Roboto:wght@400;500&display=swap" rel="stylesheet">
<style>
  :root {
    --backdrop: #2e2622;
    --card-white: #ffffff;
    --card-black: #0d0d0d;
    --ink: #1a1a1a;
    --ink-soft: #333333;
    --gold: #b8923f;
    --rule: #8a8a8a;
    --on-black: #f4f4f4;
  }
  * { margin: 0; padding: 0; box-sizing: border-box; }
  html, body { width: 1200px; height: 900px; overflow: hidden; }
  body {
    background: var(--backdrop);
    font-family: "Roboto", Arial, sans-serif;
    position: relative;
  }
  .card {
    position: absolute;
    top: 290px;
    width: 540px;
    height: 310px;
    border-radius: 3px;
    box-shadow: 0 14px 30px rgba(0,0,0,.45);
    overflow: hidden;
  }
  .card--front { left: 50px; background: var(--card-white); }
  .card--back  { left: 610px; background: var(--card-black); display: flex; align-items: center; justify-content: center; }

  .brand-name {
    font-family: "Michroma", "Arial Black", sans-serif;
    font-weight: 400;
    letter-spacing: 1px;
    white-space: nowrap;
  }
  .card--front .brand-name {
    position: absolute;
    left: 28px;
    top: 72px;
    font-size: 36px;
    color: var(--ink);
  }
  .card--back .brand-name {
    font-size: 30px;
    color: var(--on-black);
  }

  .rule { position: absolute; height: 1px; background: var(--rule); }
  .rule--upper { left: 250px; right: 28px; top: 140px; }
  .rule--lower { left: 28px; right: 28px; top: 228px; }

  .contact-row {
    position: absolute;
    left: 28px;
    right: 28px;
    top: 160px;
    height: 52px;
    display: flex;
    align-items: center;
  }
  .holder-name {
    font-family: "Michroma", "Arial Black", sans-serif;
    font-size: 16px;
    color: var(--gold);
    white-space: nowrap;
  }
  .divider {
    width: 1px;
    height: 30px;
    background: var(--gold);
    margin: 0 12px;
    flex: none;
  }
  .contact-list { list-style: none; font-size: 11.5px; color: var(--ink-soft); line-height: 19px; }
  .contact-list li { display: flex; align-items: center; gap: 5px; white-space: nowrap; }
  .icon { width: 11px; height: 11px; flex: none; }
  .icon path, .icon rect, .icon circle { fill: none; stroke: var(--gold); stroke-width: 1.4; }

  .address {
    position: absolute;
    left: 28px;
    right: 28px;
    top: 240px;
    font-size: 10.5px;
    color: var(--ink);
    white-space: nowrap;
  }
</style>
</head>
<body>
  <section class="card card--front" aria-label="Business card front">
    <div class="brand-name">BRIVAN CASES</div>
    <div class="rule rule--upper"></div>
    <div class="contact-row">
      <div class="holder-name">MARK DUNSLEY</div>
      <div class="divider"></div>
      <ul class="contact-list">
        <li>
          <svg class="icon" viewBox="0 0 12 12" aria-hidden="true"><rect x="3" y="1" width="6" height="10" rx="1"/></svg>
          027 512 4068
        </li>
        <li>
          <svg class="icon" viewBox="0 0 12 12" aria-hidden="true"><path d="M2 1.5 L4.5 1.5 L5.5 4 L4 5 Q5 7.5 7 8 L8 6.5 L10.5 7.5 L10.5 10 Q5 10.5 2 5 Z"/></svg>
          09 528 3916
        </li>
      </ul>
      <div class="divider"></div>
      <ul class="contact-list">
        <li>
          <svg class="icon" viewBox="0 0 12 12" aria-hidden="true"><rect x="1" y="2.5" width="10" height="7"/><path d="M1 2.5 L6 6.5 L11 2.5"/></svg>
          sales@brivancases.co.nz
        </li>
        <li>
          <svg class="icon" viewBox="0 0 12 12" aria-hidden="true"><circle cx="6" cy="6" r="4.8"/><path d="M1.2 6 H10.8 M6 1.2 Q3 6 6 10.8 M6 1.2 Q9 6 6 10.8"/></svg>
          www.brivancases.co.nz
        </li>
      </ul>
    </div>
    <div class="rule rule--lower"></div>
    <p class="address">3/17 Harlow Street, Pinecrest Flats, Auckland, 0614 | PO Box 204377, Fernside, Auckland 0731</p>
  </section>

  <section class="card card--back" aria-label="Business card back">
    <div class="brand-name">BRIVAN CASES</div>
  </section>
</body>
</html>
```